Corvint Property Management Vendor Recruiting Email

We need a digital flyer to email and post on Social media to attract new vendors to our website to apply to complete maintenance work on our clients homes. I have one flyer we had produced recently that we are un-happy with. It is attached.

The example given is what we do not want!! We do not want any of the pictures used from the existing one

Target Market(s)

Construction companies and handyman

Industry/Entity Type

Residential maintenance and repairs

Requirements
Must have
• Join our team as the header not become a vendor

```html
<!DOCTYPE html>
<html lang="en">
<head>
<meta charset="utf-8">
<title>Corvint Property Management – Join Our Team</title>
<link href="https://fonts.googleapis.com/css2?family=Montserrat:wght@300;400;500;600;700;800&display=swap" rel="stylesheet">
<style>
  :root{
    --page:#e7e7e9;
    --sheet:#f0f0f0;
    --night:#16161f;
    --night-soft:#2c3240;
    --sky:#1fb8ec;
    --plum:#a34ca9;
    --ink:#16161c;
    --white:#ffffff;
    --vest:#e8642a;
  }
  *{box-sizing:border-box;margin:0;padding:0}
  html,body{width:1200px;height:1198px;overflow:hidden;background:var(--page);font-family:"Montserrat",sans-serif;color:var(--ink)}
  .flyer{position:absolute;left:150px;top:17px;width:900px;height:1163px;background:var(--sheet);overflow:hidden;box-shadow:0 2px 8px rgba(0,0,0,.18)}
  .hero{position:absolute;left:0;top:0;width:900px;height:598px;
    background:radial-gradient(ellipse 300px 260px at 40px 400px,var(--night-soft),transparent 70%),linear-gradient(160deg,#22252f 0%,var(--night) 60%,#0d0d14 100%)}
  .hero-photo{position:absolute;left:359px;top:0;width:541px;height:598px;
    background:radial-gradient(ellipse 120px 90px at 330px 80px,rgba(235,240,245,.55),transparent 75%),
               radial-gradient(ellipse 210px 260px at 300px 420px,rgba(232,100,42,.65),transparent 75%),
               linear-gradient(180deg,rgba(30,32,44,.2),rgba(18,18,26,.4))}
  .brand{position:absolute;left:47px;top:72px;display:flex;flex-direction:column;align-items:center;width:180px}
  .brand-mark{width:54px;height:54px;background:var(--sky);margin-bottom:14px}
  .brand-name{color:var(--white);font-weight:700;font-size:17px;line-height:1.25;text-align:center;letter-spacing:.06em;text-transform:uppercase}
  .join{position:absolute;left:54px;top:262px;color:var(--white);font-weight:400;font-size:60px;letter-spacing:.02em}
  .team{position:absolute;left:60px;top:330px;width:792px;display:flex;justify-content:space-between;color:var(--white);font-weight:800;font-size:204px;line-height:1}
  .requirements{position:absolute;left:456px;top:539px;width:397px;height:555px;background:var(--sky);padding:32px 42px 0 36px}
  .requirements h2{margin-left:34px;color:var(--white);font-weight:700;font-size:36px;line-height:43px}
  .req-list{list-style:none;margin-top:18px}
  .req-item{display:flex;align-items:center;font-weight:500;font-size:19.5px;line-height:23.5px;color:var(--ink)}
  .req-num{width:34px;font-weight:700;font-size:24px;flex:none}
  .req-text{flex:1;padding:9px 0;border-bottom:1px solid rgba(22,22,28,.55)}
  .req-item:last-child .req-text{border-bottom:none}
  .perks{position:absolute;left:56px;top:632px;width:380px}
  .perk{display:flex;gap:18px;margin-bottom:20px;font-size:19px;line-height:23.5px}
  .perk-icon{width:87px;height:87px;flex:none;display:flex;align-items:center;justify-content:center}
  .perk-icon.dark{background:var(--night)}
  .perk-icon.sky{background:var(--sky)}
  .perk-icon.plum{background:var(--plum)}
  .perk-text{padding-top:8px}
  .hl-plum{color:var(--plum);font-weight:700}
  .hl-sky{color:var(--sky);font-weight:700}
  .contact{position:absolute;left:47px;top:974px}
  .contact h3{font-weight:300;font-size:54px;letter-spacing:.01em}
  .phone{display:flex;align-items:center;gap:10px;margin-top:2px;font-weight:700;font-size:31px}
  .web{margin-left:50px;font-weight:700;font-size:15.5px;margin-top:2px}
</style>
</head>
<body>
<main class="flyer">
  <section class="hero">
    <div class="hero-photo" role="img" aria-label="Photo of a contractor in a white hard hat, safety glasses and orange high-visibility vest"></div>
    <div class="brand">
      <div class="brand-mark"></div>
      <div class="brand-name">Corvint<br>Property Management</div>
    </div>
    <p class="join">JOIN OUR</p>
    <h1 class="team"><span>T</span><span>E</span><span>A</span><span>M</span></h1>
  </section>

  <section class="perks">
    <div class="perk">
      <div class="perk-icon dark">
        <svg width="52" height="52" viewBox="0 0 52 52"><path d="M26 3l5 4 6-1 2 6 6 3-1 6 4 5-4 5 1 6-6 3-2 6-6-1-5 4-5-4-6 1-2-6-6-3 1-6-4-5 4-5-1-6 6-3 2-6 6 1z" fill="#fff"/><circle cx="26" cy="26" r="13" fill="none" stroke="#16161f" stroke-width="3"/><path d="M20 26l4 4 8-8" fill="none" stroke="#16161f" stroke-width="3" stroke-linecap="round" stroke-linejoin="round"/></svg>
      </div>
      <p class="perk-text"><span class="hl-plum">95% approval rating</span> on all submitted estimates. Guaranteed work volume.</p>
    </div>
    <div class="perk">
      <div class="perk-icon sky">
        <svg width="60" height="50" viewBox="0 0 60 50"><g transform="rotate(-35 30 25)"><rect x="4" y="12" width="52" height="28" rx="3" fill="#fff"/><circle cx="30" cy="26" r="7" fill="#1fb8ec"/></g></svg>
      </div>
      <p class="perk-text"><span class="hl-sky">Material purchasing program</span> to help vendors with low capital or no or bad credit.</p>
    </div>
    <div class="perk">
      <div class="perk-icon plum">
        <svg width="56" height="56" viewBox="0 0 56 56"><path d="M18 8h14l-4 8h-6z" fill="#fff"/><path d="M22 17h6c10 4 14 14 12 24-1 6-6 8-12 8h-6c-8 0-13-3-13-10 0-10 6-18 13-22z" fill="#fff"/><text x="16" y="40" font-family="Montserrat,sans-serif" font-weight="700" font-size="16" fill="#a34ca9">$</text><path d="M38 30l9 3v7c0 5-4 8-9 10-5-2-9-5-9-10v-7z" fill="#fff" stroke="#a34ca9" stroke-width="2"/><path d="M34 39l3 3 5-6" fill="none" stroke="#a34ca9" stroke-width="2.4" stroke-linecap="round"/></svg>
      </div>
      <p class="perk-text"><span class="hl-plum">Weekly secure direct deposit</span> with net 30 payment terms.</p>
    </div>
  </section>

  <section class="contact">
    <h3>Contact</h3>
    <div class="phone">
      <svg width="36" height="36" viewBox="0 0 24 24"><path d="M6.6 10.8a15 15 0 006.6 6.6l2.2-2.2a1 1 0 011-.25 11.4 11.4 0 003.6.57 1 1 0 011 1V20a1 1 0 01-1 1A17 17 0 013 4a1 1 0 011-1h3.5a1 1 0 011 1c0 1.25.2 2.45.57 3.6a1 1 0 01-.25 1z" fill="#a34ca9"/></svg>
      <span>731-555-0148</span>
    </div>
    <p class="web">www.corvintpropertymanagement.com</p>
  </section>

  <section class="requirements">
    <h2>Requirements To Become A Vendor</h2>
    <ol class="req-list">
      <li class="req-item"><span class="req-num">1.</span><span class="req-text">Auto insurance</span></li>
      <li class="req-item"><span class="req-num">2.</span><span class="req-text">Certificate of general liability insurance</span></li>
      <li class="req-item"><span class="req-num">3.</span><span class="req-text">Workman's compensation or state-issued exemption letter</span></li>
      <li class="req-item"><span class="req-num">4.</span><span class="req-text">Drive license or state-issued ID card</span></li>
      <li class="req-item"><span class="req-num">5.</span><span class="req-text">Coverage area</span></li>
      <li class="req-item"><span class="req-num">6.</span><span class="req-text">Any specialty licenses</span></li>
    </ol>
  </section>
</main>
</body>
</html>
```